Machining Business Order Thank You Insert

I am looking for a business style card to include with orders that I ship. The card needs to thank the recipient for their order, and encourage them to leave a review. The card should include my business name and contact information and have an area to hand write a message.

I mainly sale on Crafvine and my own website. We are a machining an manufacturing business that are in the sale of mostly metal machined and 3d printed plastic products.

The front of the card should include the following:
Logo: (attached)
Snapgrid: https://www.instagram.com/quillforge/
Friendwall: https://www.facebook.com/QuillForge
Website: https://www.quillforge-example.com/

The back of the card needs an area to write a message

Industry/Entity Type

3D Printing, Machining, Crafvine

Contact Information for Business Card

Black or white front, white back to write a personal message

Font styles to use
Sans Serif

Colors

Designer to choose colors to be used in the design.

Requirements
Must have
• Encourage a review, social media info

```html
<!DOCTYPE html>
<html lang="en">
<head>
<meta charset="utf-8">
<title>QuillForge – Order Thank You Card</title>
<link rel="stylesheet" href="https://fonts.googleapis.com/css2?family=Exo+2:wght@400;600&family=Montserrat:wght@400;600;700&display=swap">
<style>
  :root {
    --canvas: #9a9a98;
    --card-dark: #222221;
    --card-dark-edge: #2c2c2b;
    --accent: #e8572a;
    --ink-light: #f2f2f2;
    --ink-muted: #8d8d8d;
    --ink-dark: #555555;
    --band: #f7f7f7;
    --rule: #c9c9c9;
  }
  * { margin: 0; padding: 0; box-sizing: border-box; }
  html, body { width: 1200px; height: 675px; overflow: hidden; }
  body {
    background: var(--canvas);
    font-family: "Montserrat", sans-serif;
    position: relative;
  }
  .card {
    position: absolute;
    top: 188px;
    width: 525px;
    height: 300px;
    border-radius: 16px;
    overflow: hidden;
    background: linear-gradient(135deg, var(--card-dark) 0%, var(--card-dark-edge) 55%, var(--card-dark) 100%);
    box-shadow: 0 10px 24px rgba(0,0,0,.3);
  }
  .card--front { left: 50px; }
  .card--back { left: 625px; }

  /* Brand name lockup */
  .brand {
    position: absolute;
    display: flex;
    align-items: center;
    gap: 10px;
    white-space: nowrap;
  }
  .brand__mark {
    width: 16px; height: 16px;
    background: var(--accent);
  }
  .brand__name {
    font-family: "Exo 2", sans-serif;
    font-weight: 600;
    font-size: 26px;
    letter-spacing: 7px;
    color: var(--ink-muted);
  }
  .card--front .brand { left: 44px; top: 92px; }

  .thanks-line {
    position: absolute; left: 44px; top: 136px;
    font-size: 12px; font-weight: 600; color: var(--ink-light);
  }

  /* Person */
  .person { position: absolute; left: 330px; top: 62px; }
  .person__name {
    font-weight: 600; font-size: 22px; color: var(--accent); letter-spacing: .5px;
  }
  .person__role { font-weight: 600; font-size: 12px; color: var(--ink-light); }

  /* Contact list */
  .contact {
    position: absolute; left: 282px; top: 188px;
    list-style: none;
  }
  .contact__item {
    display: flex; align-items: center; gap: 10px;
    font-size: 13px; color: var(--ink-light);
    margin-bottom: 10px;
    white-space: nowrap;
  }
  .contact__icon {
    width: 18px; height: 18px; border-radius: 3px;
    background: var(--accent);
    display: flex; align-items: center; justify-content: center;
    flex-shrink: 0;
  }

  /* Socials */
  .socials {
    position: absolute; left: 44px; top: 216px;
    list-style: none; display: flex; gap: 16px;
  }
  .socials__item {
    display: flex; align-items: center; gap: 6px;
    font-size: 12px; font-weight: 600; color: var(--ink-light);
  }
  .socials__dot { width: 12px; height: 12px; background: var(--accent); border-radius: 2px; }

  /* Back: writing band */
  .message-band {
    position: absolute;
    left: 130px; top: 0;
    width: 220px; height: 300px;
    background: var(--band);
    transform: skewX(-25deg);
    overflow: hidden;
  }
  .message-band__rule {
    position: absolute; left: 0; right: 0;
    border-bottom: 1px solid var(--rule);
  }
  .back-text {
    position: absolute;
    width: 220px;
    text-align: center;
    white-space: nowrap;
  }
  .back-text--thanks {
    left: 186px; top: 22px;
    font-size: 12px; font-weight: 700; color: var(--accent); letter-spacing: .5px;
  }
  .back-text--label {
    left: 176px; top: 50px;
    font-size: 11px; font-weight: 600; letter-spacing: 1.5px; color: var(--ink-dark);
  }
  .back-text--review {
    left: 81px; top: 250px;
    font-size: 11px; font-weight: 600; color: var(--ink-dark);
  }
  .card--back .brand { left: 330px; top: 246px; gap: 8px; }
  .card--back .brand__mark { width: 13px; height: 13px; }
  .card--back .brand__name { font-size: 17px; letter-spacing: 4px; }
</style>
</head>
<body>

<section class="card card--front" aria-label="Card front">
  <div class="brand">
    <span class="brand__mark"></span>
    <span class="brand__name">QUILLFORGE</span>
  </div>
  <p class="thanks-line">Thank you for your order!</p>

  <div class="person">
    <p class="person__name">NAME</p>
    <p class="person__role">Designation</p>
  </div>

  <ul class="socials">
    <li class="socials__item"><span class="socials__dot"></span>Friendwall</li>
    <li class="socials__item"><span class="socials__dot"></span>Snapgrid</li>
  </ul>

  <ul class="contact">
    <li class="contact__item">
      <span class="contact__icon">
        <svg width="10" height="12" viewBox="0 0 10 12"><path d="M5 0a4 4 0 0 0-4 4c0 3 4 8 4 8s4-5 4-8a4 4 0 0 0-4-4zm0 5.5A1.5 1.5 0 1 1 5 2.5a1.5 1.5 0 0 1 0 3z" fill="#222"/></svg>
      </span>
      Millbrook, Ohio
    </li>
    <li class="contact__item">
      <span class="contact__icon">
        <svg width="11" height="11" viewBox="0 0 12 12"><path d="M2.5 0.5l2 2.5-1.2 1.3a7 7 0 0 0 4.4 4.4L9 7.5l2.5 2-1.2 2C5 11.5 .5 7 .5 1.7z" fill="#222"/></svg>
      </span>
      xxx-xxx-xxxx
    </li>
    <li class="contact__item">
      <span class="contact__icon">
        <svg width="12" height="12" viewBox="0 0 12 12" fill="none" stroke="#222" stroke-width="1.2"><circle cx="6" cy="6" r="5"/><ellipse cx="6" cy="6" rx="2.2" ry="5"/><path d="M1 6h10"/></svg>
      </span>
      www.quillforge-example.com
    </li>
  </ul>
</section>

<section class="card card--back" aria-label="Card back">
  <div class="message-band">
    <span class="message-band__rule" style="top:100px"></span>
    <span class="message-band__rule" style="top:130px"></span>
    <span class="message-band__rule" style="top:160px"></span>
    <span class="message-band__rule" style="top:190px"></span>
    <span class="message-band__rule" style="top:220px"></span>
  </div>
  <p class="back-text back-text--thanks">THANK YOU FOR YOUR ORDER</p>
  <p class="back-text back-text--label">MESSAGE</p>
  <p class="back-text back-text--review">Loved it? Leave us a review on Crafvine!</p>
  <div class="brand">
    <span class="brand__mark"></span>
    <span class="brand__name">QUILLFORGE</span>
  </div>
</section>

</body>
</html>
```